Lena Corvell Business Card

I need a business card that reflects my current website: itslenacorvell.example and screenshot attached. If we keep the color scheme of the site and sample card below that would be ideal. The business card should include the information on the attached sample cards.

Industry/Entity Type

Business

```html
<!DOCTYPE html>
<html lang="en">
<head>
<meta charset="utf-8">
<title>Lena Corvell – Business Card</title>
<link rel="stylesheet" href="https://fonts.googleapis.com/css2?family=Open+Sans:wght@400;600&display=swap">
<style>
  :root {
    --page-bg: #ffffff;
    --card-teal: #5fbfae;
    --card-charcoal: #545150;
    --ink: #4a4847;
    --ornament: #4f4442;
  }
  * { margin: 0; padding: 0; box-sizing: border-box; }
  html, body {
    width: 1200px;
    height: 893px;
    overflow: hidden;
    background: var(--page-bg);
    font-family: "Open Sans", Arial, sans-serif;
  }
  .canvas {
    position: relative;
    width: 1200px;
    height: 893px;
  }
  .business-card {
    position: absolute;
    left: 299px;
    top: 230px;
    width: 594px;
    height: 330px;
    background: var(--card-teal);
    overflow: hidden;
  }
  .card-wave {
    position: absolute;
    inset: 0;
    width: 594px;
    height: 330px;
  }
  .contact-block {
    position: absolute;
    left: 30px;
    top: 34px;
    color: var(--ink);
  }
  .contact-name {
    font-size: 23px;
    font-weight: 400;
    letter-spacing: 0.2px;
    line-height: 1;
  }
  .contact-roles {
    margin-top: 14px;
    font-size: 18.5px;
    line-height: 1;
  }
  .contact-line {
    font-size: 14px;
    line-height: 1;
    margin-top: 16px;
  }
  .contact-line.first { margin-top: 18px; }
  .bow-ornament {
    position: absolute;
    left: 88px;
    top: 230px;
    width: 107px;
    height: 74px;
    border-radius: 30px 30px 14px 14px;
    background: var(--ornament);
  }
  .brand-wordmark {
    position: absolute;
    left: 348px;
    top: 258px;
    font-size: 34px;
    font-weight: 400;
    color: var(--card-teal);
    line-height: 1;
    white-space: nowrap;
  }
</style>
</head>
<body>
<main class="canvas">
  <section class="business-card" aria-label="Lena Corvell business card">
    <svg class="card-wave" viewBox="0 0 594 330" aria-hidden="true">
      <path d="M0,166 C15,260 70,330 160,328 C260,326 330,262 440,234 C510,216 560,218 594,222 L594,330 L0,330 Z" fill="var(--card-charcoal)"/>
    </svg>

    <div class="contact-block">
      <h1 class="contact-name">LENA CORVELL</h1>
      <p class="contact-roles">Brand Curator I Digital Storyteller I Social Entrpreneuer</p>
      <p class="contact-line first">me@lenacorvell.example</p>
      <p class="contact-line">[fb] I [t.] I [ig] @itslenacorvell</p>
      <p class="contact-line">www.itslenacorvell.example</p>
    </div>

    <div class="bow-ornament" role="img" aria-label="Decorative ribbon bow ornament"></div>

    <p class="brand-wordmark">Lena Corvell</p>
  </section>
</main>
</body>
</html>
```